Dane Morrow Photography Business Card

I am looking for a simple, yet elegant business card for my photography business.

It is a short turn around project as the cards need to be printed within 48 hours. So the earlier you submit, the more likely you are to be chosen.

I am a professional portrait, sports and commercial photographer located in Brisbane, Australia. I am looking for a professional business card to distribute to professional clients. The card needs to be professional and easy to read. It must have my contact information as listed below.

Industry/Entity Type

Business

Contact Information for Business Card

Dane Morrow Photography
www.danemorrowphoto.com.au
dane@danemorrowphoto.com.au
+61 437 280 556

Font styles to use
Serif
Sans Serif

Colors
ffc214
fece3e
fee18a

Requirements
Must have
• Must have contact information as above,
• Please use a similar colourscheme to the one provided in the logo upload.
Nice to have
• A very simple, design, happy to have some geometric shapes etc. Must look professional

```html
<!DOCTYPE html>
<html lang="en">
<head>
<meta charset="utf-8">
<title>Dane Morrow Photography – Business Card</title>
<link rel="stylesheet" href="https://fonts.googleapis.com/css2?family=Nunito+Sans:wght@300&display=swap">
<style>
  :root {
    --card-bg: #ebebec;
    --band-dark: #3a3a3c;
    --ink: #4a4a4c;
    --ink-light: #d6d6d8;
    --gold: #d98f1f;
    --gold-light: #f0ac2e;
  }
  * { margin: 0; padding: 0; box-sizing: border-box; }
  html, body {
    width: 1200px;
    height: 686px;
    overflow: hidden;
    background: var(--card-bg);
  }
  .card {
    position: relative;
    width: 1200px;
    height: 686px;
    overflow: hidden;
    font-family: "Nunito Sans", "Helvetica Neue", Arial, sans-serif;
    font-weight: 300;
    color: var(--ink);
  }
  .card__pattern {
    position: absolute;
    inset: 0;
    background: var(--card-bg);
  }
  .card__bands {
    position: absolute;
    inset: 0;
  }
  .brand-mark {
    position: absolute;
    left: 166px;
    top: 227px;
    width: 230px;
    height: 230px;
    border-radius: 50%;
    background: radial-gradient(circle at 35% 30%, var(--gold-light), var(--gold));
  }
  .brand-name {
    position: absolute;
    left: 0;
    top: 0;
    width: 100%;
    height: 100%;
    font-weight: 300;
    line-height: 1;
    text-transform: uppercase;
    white-space: nowrap;
  }
  .brand-name__primary {
    position: absolute;
    left: 443px;
    top: 270px;
    font-size: 96px;
    font-weight: 300;
    letter-spacing: 0.5px;
  }
  .brand-name__secondary {
    position: absolute;
    left: 447px;
    top: 366px;
    font-size: 51px;
    font-weight: 300;
    letter-spacing: 0.5px;
  }
  .contact {
    position: absolute;
    right: 60px;
    top: 628px;
    display: flex;
    gap: 34px;
    list-style: none;
    font-size: 19px;
    font-weight: 300;
    line-height: 1;
    letter-spacing: 0.4px;
    color: var(--ink-light);
    white-space: nowrap;
  }
</style>
</head>
<body>
  <main class="card">
    <div class="card__pattern" role="img" aria-label="Light grey background with a subtle repeating diamond pattern"></div>

    <svg class="card__bands" width="1200" height="686" viewBox="0 0 1200 686" aria-hidden="true">
      <path fill="var(--band-dark)" d="M95,0 C320,70 620,192 900,185 C1050,181 1150,125 1200,85 L1200,0 Z"/>
      <path fill="var(--band-dark)" d="M95,686 C320,615 620,498 880,505 C1050,510 1150,560 1200,600 L1200,686 Z"/>
    </svg>

    <div class="brand-mark" aria-hidden="true"></div>

    <h1 class="brand-name">
      <span class="brand-name__primary">Dane Morrow</span>
      <span class="brand-name__secondary">Photography</span>
    </h1>

    <ul class="contact">
      <li class="contact__web">www.danemorrowphoto.com.au</li>
      <li class="contact__email">dane@danemorrowphoto.com.au</li>
      <li class="contact__phone">+61 437 280 556</li>
    </ul>
  </main>
</body>
</html>
```